Business Card Design

I need a business card design for a new company that is based in Singapore region. The name of the company is called " Kalvaro Holdings Pte.Ltd " This company serves as a holding company that owns several types of businesses under our name. One of the established company in Singapore is the Kalvaro Food Industries that serves as a food service industry that has their own brand name which operates in malls and CBD areas. We would prefer the design of the business cards will use the colors of black as the base and red as for the designs. The final design of the name card should be able to communicate young and professional type of business culture. In which we appreciate creativity to their highest point.
Industry/Entity Type
Industry
Contact Information for Business Card
Matteo Bastian Kalvaro
Director, Founder
Contact: +65 81247760
E-mail: matteobk@quellmail.com

```html
<!DOCTYPE html>
<html lang="en">
<head>
<meta charset="utf-8">
<title>Kalvaro Holdings Pte.Ltd – Business Card</title>
<link rel="stylesheet" href="https://fonts.googleapis.com/css2?family=Source+Sans+3:wght@400&display=swap">
<style>
  :root {
    --card-black: #040607;
    --card-red: #6a0910;
    --text-light: #ffffff;
    --silver-light: #ffffff;
    --silver-mid: #b9b9b9;
    --silver-dark: #4a4a4a;
  }
  html, body {
    margin: 0;
    padding: 0;
    width: 1200px;
    height: 737px;
    overflow: hidden;
    background: var(--card-black);
  }
  .business-card {
    position: relative;
    width: 1200px;
    height: 737px;
    background: var(--card-black);
    font-family: "Source Sans 3", "Myriad Pro", sans-serif;
    color: var(--text-light);
    overflow: hidden;
  }
  .card-wave {
    position: absolute;
    inset: 0;
    width: 1200px;
    height: 737px;
  }
  .contact-block {
    position: absolute;
    left: 515px;
    top: 164px;
    font-size: 46px;
    line-height: 65px;
    letter-spacing: 0.2px;
  }
  .contact-line { margin: 0; white-space: nowrap; }
  .identity-block {
    position: absolute;
    right: 49px;
    top: 445px;
    text-align: right;
  }
  .company-name {
    margin: 0;
    font-size: 44px;
    line-height: 52px;
  }
  .person-name {
    margin: 0;
    font-size: 76px;
    line-height: 80px;
    letter-spacing: 0.3px;
  }
  .person-title {
    margin: 0;
    font-size: 26px;
    line-height: 32px;
  }
</style>
</head>
<body>
  <main class="business-card">
    <svg class="card-wave" viewBox="0 0 1200 737" aria-hidden="true">
      <defs>
        <linearGradient id="silver-edge" x1="0" y1="0" x2="1200" y2="0" gradientUnits="userSpaceOnUse">
          <stop offset="0" stop-color="var(--silver-light)"/>
          <stop offset="0.35" stop-color="var(--silver-mid)"/>
          <stop offset="0.6" stop-color="#9a9a9a"/>
          <stop offset="1" stop-color="var(--silver-dark)"/>
        </linearGradient>
      </defs>
      <path class="wave-red" fill="var(--card-red)"
            d="M0,418 C90,478 190,498 310,484 C440,468 530,350 720,340 C880,333 1030,366 1200,418 L1200,737 L0,737 Z"/>
      <path class="wave-edge" fill="none" stroke="url(#silver-edge)" stroke-width="9"
            d="M0,414 C90,474 190,494 310,480 C440,464 530,346 720,336 C880,329 1030,362 1200,414"/>
    </svg>

    <section class="contact-block">
      <p class="contact-line">Telephone: +65 81247760</p>
      <p class="contact-line">Email: matteobk@quellmail.com</p>
    </section>

    <section class="identity-block">
      <p class="company-name">Kalvaro Holdings Pte.Ltd</p>
      <h1 class="person-name">Matteo Bastian Kalvaro</h1>
      <p class="person-title">Director and Founder</p>
    </section>
  </main>
</body>
</html>
```